Accounting Practice Business Card Design

I have a logo I am happy for you to use in the design of the Business Card.
You can edit and change colours as you please, I am not fixated on it.
I am looking for a modern and clean overall feel for the finished design.

The business is a small accounting practice who thrives on word of mouth referrals and this card will be given to all current and prospect clients.

Industry/Entity Type

Accountant

Contact Information for Business Card

Marcus Elwin
Level 5, 8 Corvale Ridge Road
ASHGROVE RISE VIC 3187
Phone: 9481 3057
Email: melwin@mrfaccountants.com.au
Web: www.mrfaccountants.com.au

Font styles to use
Serif
Sans Serif

Colors
0555a3
3277b5
85acd3
0393ce
33a6d7
85cae6
00a990
33b8a4
9bcb3c

Requirements
Must have
• "The end to your tax problems begin with us"
• "A referral from you is our greatest compliment"
Nice to have
• Modern clean professional

```html
<!DOCTYPE html>
<html lang="en">
<head>
<meta charset="utf-8">
<title>MRF Accountants – Business Card</title>
<link rel="stylesheet" href="https://fonts.googleapis.com/css2?family=Source+Sans+3:wght@400;700&display=swap">
<style>
  :root {
    --page: #fdfdfd;
    --paper: #f2f2f2;
    --sky: #35a4d7;
    --ocean: #0593ce;
    --rule: #0555a3;
    --navy: #13477a;
    --ink: #0a8fc8;
    --white: #ffffff;
  }
  * { margin: 0; padding: 0; box-sizing: border-box; }
  html, body { width: 1200px; height: 1200px; overflow: hidden; background: var(--page); }
  body { position: relative; font-family: "Source Sans 3", sans-serif; }

  .card-back, .card-front { position: absolute; top: 193px; height: 839px; width: 480px; }
  .card-back { left: 121px; background: var(--paper); }
  .card-front { left: 601px; background: var(--paper); }

  .band { position: absolute; left: 0; width: 100%; }
  .band--top { top: 0; height: 261px; background: var(--sky); border-bottom: 4px solid var(--rule); }
  .band--bottom { top: 544px; height: 295px; background: var(--ocean); border-top: 4px solid var(--rule); }

  .wordmark {
    position: absolute; left: 0; width: 100%;
    text-align: center; color: var(--navy); font-weight: 700; line-height: 1;
  }
  .wordmark__name { display: block; font-size: 118px; letter-spacing: 2px; }
  .wordmark__trade { display: block; font-size: 36px; letter-spacing: 3px; margin-top: 4px; }
  .card-back .wordmark { top: 338px; }
  .card-front .wordmark { top: 56px; }

  .name-bar {
    position: absolute; top: 261px; left: 0; width: 100%; height: 54px;
    background: var(--ocean); color: var(--white);
    font-size: 32px; line-height: 54px; text-align: center;
    box-shadow: 0 4px 5px rgba(0,0,0,0.35);
  }

  .contact { position: absolute; left: 62px; top: 535px; list-style: none; color: var(--ink); font-size: 26px; line-height: 33px; }
  .contact__item { position: relative; padding-left: 34px; margin-bottom: 24px; }
  .contact__item svg { position: absolute; left: -6px; top: 2px; width: 34px; height: 34px; }
  .contact__item--address { margin-top: 26px; }
</style>
</head>
<body>
  <section class="card-back">
    <div class="band band--top"></div>
    <div class="wordmark"><span class="wordmark__name">MRF</span><span class="wordmark__trade">ACCOUNTANTS</span></div>
    <div class="band band--bottom"></div>
  </section>

  <section class="card-front">
    <div class="wordmark"><span class="wordmark__name">MRF</span><span class="wordmark__trade">ACCOUNTANTS</span></div>
    <div class="name-bar">Marcus Elwin</div>

    <ul class="contact">
      <li class="contact__item">
        <svg viewBox="0 0 34 34"><path d="M6 4c3-2 5-1 6 2l2 4c1 2 0 3-2 4 1 4 4 7 8 9 1-2 2-3 4-2l4 2c3 1 3 3 1 6-3 3-8 3-14-2S2 11 6 4z" fill="var(--ink)"/></svg>
        9481 3057
      </li>
      <li class="contact__item">
        <svg viewBox="0 0 34 34"><rect x="2" y="9" width="30" height="18" fill="none" stroke="var(--ink)" stroke-width="2.5"/><path d="M2 9l15 11 15-11M2 27l11-9M32 27l-11-9" fill="none" stroke="var(--ink)" stroke-width="2"/></svg>
        melwin@mrfaccountants.com.au
      </li>
      <li class="contact__item">
        <svg viewBox="0 0 34 34"><circle cx="17" cy="17" r="14" fill="none" stroke="var(--ink)" stroke-width="2.5"/><ellipse cx="17" cy="17" rx="6" ry="14" fill="none" stroke="var(--ink)" stroke-width="2"/><path d="M3 17h28M6 10h22M6 24h22" stroke="var(--ink)" stroke-width="2"/></svg>
        www.mrfaccountants.com.au
      </li>
      <li class="contact__item contact__item--address">
        <svg viewBox="0 0 34 34"><path d="M17 2a10 10 0 0 0-10 10c0 8 10 20 10 20s10-12 10-20A10 10 0 0 0 17 2z" fill="var(--ink)"/><circle cx="17" cy="11" r="4" fill="var(--white)"/></svg>
        Level 5, 8 Corvale Ridge Road<br>ASHGROVE RISE VIC 3187
      </li>
    </ul>
  </section>
</body>
</html>
```